House mailers

I want an informative flyer that has ou logo on the top right with our lic number photos and a description of our services. I also want the back to say tip of the moth with only two photos I will provide. clean setup noting crowded. sample flyer below.

```html
<!DOCTYPE html>
<html lang="en">
<head>
<meta charset="utf-8">
<title>House Mailer – Residential Seismic Retrofit</title>
<link rel="stylesheet" href="https://fonts.googleapis.com/css2?family=Lato:wght@700;900&family=Roboto:wght@400;500;700&display=swap">
<style>
  :root{
    --stage:#f3f6fc;
    --paper:#ffffff;
    --brand-blue:#0a63f5;
    --brand-red:#d3121f;
    --navy:#0b1734;
    --ink:#2b2f38;
    --muted:#6b7080;
    --photo-wood:#8a6a48;
    --photo-dark:#2a2620;
    --photo-glove:#5d6474;
    --photo-stucco:#a9a7a0;
    --photo-stone:#b58a6e;
  }
  *{box-sizing:border-box;margin:0;padding:0}
  html,body{width:1200px;height:783px;overflow:hidden;background:var(--stage)}
  body{position:relative;font-family:"Roboto",Arial,sans-serif;color:var(--ink)}

  .page{position:absolute;top:71px;width:496px;height:642px;background:var(--paper);
        box-shadow:0 6px 18px rgba(30,50,100,.12);overflow:hidden}
  .page--front{left:78px}
  .page--back{left:626px}

  .brand{position:absolute;top:16px;right:28px;display:flex;align-items:flex-start;gap:5px}
  .brand__square{width:18px;height:18px;background:var(--brand-blue);margin-top:2px}
  .brand__text{display:flex;flex-direction:column;align-items:flex-end}
  .brand__name{font-family:"Lato",Arial,sans-serif;font-weight:900;color:var(--brand-blue);
        font-size:11px;line-height:11px;letter-spacing:.3px;text-align:right}
  .brand__license{font-family:"Roboto",Arial,sans-serif;font-size:3.6px;color:var(--navy);margin-top:2px}

  /* front */
  .hero-band{position:absolute;left:179px;top:63px;right:0;height:196px;background:var(--brand-blue)}
  .hero-ring{position:absolute;left:-57px;top:25px;width:272px;height:272px;border-radius:50%;
        background:var(--paper);border:4px solid var(--brand-red)}
  .hero-photo{position:absolute;left:-47px;top:35px;width:252px;height:252px;border-radius:50%;
        background:radial-gradient(circle at 55% 55%,var(--photo-glove) 0 22%,var(--photo-wood) 45%,var(--photo-dark) 100%)}
  .hero-title{position:absolute;left:247px;top:95px;font-family:"Lato",Arial,sans-serif;font-weight:700;
        color:#fff;font-size:20.5px;line-height:24px;letter-spacing:.2px}
  .hero-rule{position:absolute;left:218px;top:151px;width:76px;height:1.5px;background:#fff}
  .hero-rule::after{content:"";position:absolute;right:-4px;top:-3.5px;width:8px;height:8px;border-radius:50%;background:#fff}
  .hero-sub{position:absolute;left:247px;top:168px;color:#fff;font-weight:500;font-size:8.4px;text-decoration:underline}
  .hero-copy{position:absolute;left:247px;top:188px;width:220px;color:#fff;font-size:6.4px;line-height:9.8px;text-align:justify}
  .hero-copy strong{font-weight:700}

  .services-title{position:absolute;left:0;width:496px;top:309px;text-align:center;font-family:"Lato",Arial,sans-serif;
        font-weight:700;font-size:20px;color:var(--brand-blue)}
  .services-title__mark{position:absolute;left:237px;top:331px;width:22px;height:1.6px;background:var(--brand-red)}

  .services{position:absolute;left:29px;top:356px;display:grid;grid-template-columns:repeat(4,103px);
        grid-auto-rows:101px;column-gap:9px;row-gap:9px}
  .service{border:1px solid var(--brand-red);border-radius:3px;text-align:center;padding:7px 5px 0}
  .service:nth-child(even){border-color:var(--brand-blue)}
  .service__photo{width:39px;height:39px;border-radius:50%;margin:0 auto;
        background:radial-gradient(circle at 40% 40%,#9a8b78,#3b3630)}
  .service__name{font-weight:700;font-size:4.6px;letter-spacing:.1px;margin-top:10px;color:var(--ink)}
  .service__text{font-size:3.4px;line-height:6.2px;color:var(--muted);margin-top:5px}

  .contact-bar{position:absolute;left:0;bottom:0;width:496px;height:36px;background:var(--navy);
        display:flex;align-items:center;justify-content:center;gap:14px;color:#fff;font-size:7.6px}
  .contact{display:flex;align-items:center;gap:7px}
  .contact__icon{width:17px;height:17px;border-radius:50%;background:#fff;display:flex;align-items:center;justify-content:center}

  /* back */
  .tip-band{position:absolute;left:0;top:63px;width:496px;height:78px;background:var(--brand-blue);
        display:flex;align-items:center;justify-content:center}
  .tip-title{font-family:"Lato",Arial,sans-serif;font-weight:700;color:#fff;font-size:22.5px;letter-spacing:.2px}
  .tip-photo{position:absolute;left:29px;width:438px;height:197px}
  .tip-photo--crawlspace{top:175px;background:linear-gradient(160deg,var(--photo-wood) 0%,#5a4632 35%,var(--photo-dark) 70%,#4a4540 100%)}
  .tip-photo--access{top:400px;background:linear-gradient(120deg,var(--photo-stone) 0%,#9b8c80 40%,var(--photo-stucco) 70%,#8d8f95 100%)}
</style>
</head>
<body>

<section class="page page--front">
  <div class="hero-band"></div>
  <div class="hero-ring"></div>
  <div class="hero-photo" role="img" aria-label="Gloved hand holding a moisture meter against a wooden crawl space post"></div>

  <div class="brand">
    <div class="brand__square"></div>
    <div class="brand__text">
      <div class="brand__name">COASTLINE QUAKE<br>HOUSE BOLTING</div>
      <div class="brand__license">#7731204</div>
    </div>
  </div>

  <h1 class="hero-title">RESIDENTIAL<br>SEISMIC RETROFIT</h1>
  <div class="hero-rule"></div>
  <p class="hero-sub">SERVICING LOS ANGELES &amp; SURROUNDING CITIES</p>
  <p class="hero-copy"><strong>COASTLINE QUAKE</strong> is a company born out of a passion for making California a safer place. With our expertise in the knowledge of earthquake retrofitting and our hardworking team, we have been reinforcing older homes up to current code all over California.</p>

  <h2 class="services-title">OUR SERVICES</h2>
  <div class="services-title__mark"></div>

  <div class="services">
    <div class="service"><div class="service__photo" role="img" aria-label="Dark crawl space under a house"></div><h3 class="service__name">FOUNDATION INSPECTIONS</h3><p class="service__text">Older houses—those built before 1980—may not be adequately anchored to the foundation, making them more vulnerable to shaking and more likely to slide off their foundation during a quake.</p></div>
    <div class="service"><div class="service__photo" role="img" aria-label="Steel anchor plates bolted to a sill"></div><h3 class="service__name">HOUSE BOLTING</h3><p class="service__text">Older houses—those built before 1980—may not be adequately anchored to the foundation, making them more vulnerable to shaking and more likely to slide off their foundation during a quake.</p></div>
    <div class="service"><div class="service__photo" role="img" aria-label="Repaired concrete foundation wall"></div><h3 class="service__name">CRACK REPAIR</h3><p class="service__text">Older houses—those built before 1980—may not be adequately anchored to the foundation, making them more vulnerable to shaking and more likely to slide off their foundation during a quake.</p></div>
    <div class="service"><div class="service__photo" role="img" aria-label="Wood beam with metal reinforcement bracket"></div><h3 class="service__name">BEAM REINFORCEMENT</h3><p class="service__text">Older houses—those built before 1980—may not be adequately anchored to the foundation, making them more vulnerable to shaking and more likely to slide off their foundation during a quake.</p></div>
    <div class="service"><div class="service__photo" role="img" aria-label="Damaged framing in a crawl space"></div><h3 class="service__name">STRUCTURAL DEFECTS</h3><p class="service__text">Older houses—those built before 1980—may not be adequately anchored to the foundation, making them more vulnerable to shaking and more likely to slide off their foundation during a quake.</p></div>
    <div class="service"><div class="service__photo" role="img" aria-label="Plywood cripple wall with bolts"></div><h3 class="service__name">CRIPPLE WALL BRACING</h3><p class="service__text">Older houses—those built before 1980—may not be adequately anchored to the foundation, making them more vulnerable to shaking and more likely to slide off their foundation during a quake.</p></div>
    <div class="service"><div class="service__photo" role="img" aria-label="Cracked concrete slab being stitched"></div><h3 class="service__name">FOUNDATION CRACK STITCHING</h3><p class="service__text">Older houses—those built before 1980—may not be adequately anchored to the foundation, making them more vulnerable to shaking and more likely to slide off their foundation during a quake.</p></div>
    <div class="service"><div class="service__photo" role="img" aria-label="Encapsulated crawl space with vapor barrier"></div><h3 class="service__name">CRAWL SPACE ENCAPSULATION</h3><p class="service__text">Older houses—those built before 1980—may not be adequately anchored to the foundation, making them more vulnerable to shaking and more likely to slide off their foundation during a quake.</p></div>
  </div>

  <footer class="contact-bar">
    <div class="contact">
      <span class="contact__icon"><svg width="9" height="9" viewBox="0 0 24 24"><path fill="#d3121f" d="M6.6 10.8a15 15 0 0 0 6.6 6.6l2.2-2.2a1 1 0 0 1 1-.25 11.4 11.4 0 0 0 3.6.57 1 1 0 0 1 1 1V20a1 1 0 0 1-1 1A17 17 0 0 1 3 4a1 1 0 0 1 1-1h3.5a1 1 0 0 1 1 1c0 1.25.2 2.45.57 3.57a1 1 0 0 1-.25 1z"/></svg></span>
      <span>555-014-2290</span>
    </div>
    <div class="contact">
      <span class="contact__icon"><svg width="9" height="9" viewBox="0 0 24 24"><rect x="3" y="5" width="18" height="14" rx="2" fill="#d3121f"/><path d="M4 7l8 6 8-6" fill="none" stroke="#fff" stroke-width="1.8"/></svg></span>
      <span>hello@coastlinequake.com</span>
    </div>
    <div class="contact">
      <span class="contact__icon"><svg width="9" height="9" viewBox="0 0 24 24"><circle cx="12" cy="12" r="9" fill="#d3121f"/><path d="M3 12h18M12 3c3 3 3 15 0 18M12 3c-3 3-3 15 0 18" fill="none" stroke="#fff" stroke-width="1.4"/></svg></span>
      <span>www.coastlinequake.com</span>
    </div>
  </footer>
</section>

<section class="page page--back">
  <div class="brand">
    <div class="brand__square"></div>
    <div class="brand__text">
      <div class="brand__name">COASTLINE QUAKE<br>HOUSE BOLTING</div>
      <div class="brand__license">#7731204</div>
    </div>
  </div>

  <div class="tip-band"><h2 class="tip-title">TIP OF THE MONTH</h2></div>

  <div class="tip-photo tip-photo--crawlspace" role="img" aria-label="Technician testing a wooden post with a moisture meter inside a crawl space"></div>
  <div class="tip-photo tip-photo--access" role="img" aria-label="Worker entering a crawl space access opening beside a house wall"></div>
</section>

</body>
</html>
```